Sticker Design for Company Equipment - Velunora

We are looking for a professional and clean graphic design for a set of stickers to apply on our company equipment (cleaning, gardening, pest control). The stickers must include our logo (the square with the three colored segments and the checkmark), our phone number, email address, and website, you can decide to use all three or just our website based on your graphic needs. It is important that it has an attractive sharp and clear look. The design should be consistent with our brand identity and give a polished, trustworthy look to our tools and machinery. We need a modular design that works in different formats (rectangular, square, round), depending on the type of equipment.

Need extra days to review

```html
<!DOCTYPE html>
<html lang="en">
<head>
<meta charset="utf-8">
<title>Velunora – Equipment Stickers</title>
<link rel="stylesheet" href="https://fonts.googleapis.com/css2?family=Abril+Fatface&family=Lato:wght@700&display=swap">
<style>
  :root {
    --orange: #f26a25;
    --navy: #29235c;
    --green: #76c043;
    --white: #ffffff;
    --outline: #3a3a3a;
  }
  html, body {
    margin: 0;
    padding: 0;
    width: 1200px;
    height: 828px;
    overflow: hidden;
    background: var(--white);
  }
  .sheet { display: block; width: 1200px; height: 828px; }

  .sticker-edge { fill: none; stroke: var(--outline); stroke-width: 0.6; }

  .brand-name {
    font-family: "Lato", sans-serif;
    font-weight: 700;
    font-size: 27px;
    letter-spacing: 1.5px;
    text-anchor: middle;
  }
  .service-word {
    font-family: "Abril Fatface", serif;
    text-anchor: middle;
  }
  .service-word--single { font-size: 80px; }
  .service-word--stacked { font-size: 68px; }
  .contact {
    font-family: "Lato", sans-serif;
    font-weight: 700;
    font-size: 15.5px;
    text-anchor: middle;
  }

  /* light variants: white sticker, coloured accents */
  .light .sticker-bg { fill: var(--white); }
  .light .brand-name, .light .brand-square { fill: var(--navy); }
  .light.orange .service-word, .light.orange .contact-band { fill: var(--orange); }
  .light.navy .service-word, .light.navy .contact-band { fill: var(--navy); }
  .light.green .service-word, .light.green .contact-band { fill: var(--green); }
  .light .contact { fill: var(--white); }

  /* solid variants: coloured sticker, white accents */
  .solid.orange .sticker-bg, .solid.orange .contact { fill: var(--orange); }
  .solid.navy .sticker-bg, .solid.navy .contact { fill: var(--navy); }
  .solid.green .sticker-bg, .solid.green .contact { fill: var(--green); }
  .solid .brand-name, .solid .brand-square, .solid .service-word, .solid .contact-band { fill: var(--white); }
</style>
</head>
<body>
<svg class="sheet" viewBox="0 0 1200 828" xmlns="http://www.w3.org/2000/svg">
  <defs>
    <clipPath id="sticker-shape">
      <circle cx="0" cy="0" r="176"/>
    </clipPath>
  </defs>

  <!-- Cleaning, light -->
  <g class="sticker light orange" transform="translate(213 220)">
    <g clip-path="url(#sticker-shape)">
      <circle class="sticker-bg" r="176"/>
      <path class="contact-band" d="M-200 118 Q0 64 200 118 L200 200 L-200 200 Z"/>
    </g>
    <circle class="sticker-edge" r="176"/>
    <rect class="brand-square" x="-18" y="-156" width="36" height="36"/>
    <text class="brand-name" y="-80">VELUNORA</text>
    <text class="service-word service-word--single" y="36" textLength="305" lengthAdjust="spacingAndGlyphs">Cleaning</text>
    <text class="contact" y="115">+39 320 5550147</text>
    <text class="contact" y="132">officevelunora.srl</text>
    <text class="contact" y="149">www.velunora.srl</text>
  </g>

  <!-- Gardening, light -->
  <g class="sticker light navy" transform="translate(600 220)">
    <g clip-path="url(#sticker-shape)">
      <circle class="sticker-bg" r="176"/>
      <path class="contact-band" d="M-200 118 Q0 64 200 118 L200 200 L-200 200 Z"/>
    </g>
    <circle class="sticker-edge" r="176"/>
    <rect class="brand-square" x="-18" y="-156" width="36" height="36"/>
    <text class="brand-name" y="-80">VELUNORA</text>
    <text class="service-word service-word--single" y="44" textLength="335" lengthAdjust="spacingAndGlyphs">Gardening</text>
    <text class="contact" y="115">+39 320 5550147</text>
    <text class="contact" y="132">officevelunora.srl</text>
    <text class="contact" y="149">www.velunora.srl</text>
  </g>

  <!-- Pest Control, light -->
  <g class="sticker light green" transform="translate(998 220)">
    <g clip-path="url(#sticker-shape)">
      <circle class="sticker-bg" r="176"/>
      <path class="contact-band" d="M-200 118 Q0 64 200 118 L200 200 L-200 200 Z"/>
    </g>
    <circle class="sticker-edge" r="176"/>
    <rect class="brand-square" x="-18" y="-156" width="36" height="36"/>
    <text class="brand-name" y="-80">VELUNORA</text>
    <text class="service-word service-word--stacked" y="-8" textLength="120" lengthAdjust="spacingAndGlyphs">Pest</text>
    <text class="service-word service-word--stacked" y="52" textLength="255" lengthAdjust="spacingAndGlyphs" x="12">Control</text>
    <text class="contact" y="115">+39 320 5550147</text>
    <text class="contact" y="132">officevelunora.srl</text>
    <text class="contact" y="149">www.velunora.srl</text>
  </g>

  <!-- Cleaning, solid -->
  <g class="sticker solid orange" transform="translate(198 605)">
    <g clip-path="url(#sticker-shape)">
      <circle class="sticker-bg" r="176"/>
      <path class="contact-band" d="M-200 118 Q0 64 200 118 L200 200 L-200 200 Z"/>
    </g>
    <circle class="sticker-edge" r="176"/>
    <rect class="brand-square" x="-18" y="-156" width="36" height="36"/>
    <text class="brand-name" y="-80">VELUNORA</text>
    <text class="service-word service-word--single" y="36" textLength="305" lengthAdjust="spacingAndGlyphs">Cleaning</text>
    <text class="contact" y="115">+39 320 5550147</text>
    <text class="contact" y="132">officevelunora.srl</text>
    <text class="contact" y="149">www.velunora.srl</text>
  </g>

  <!-- Gardening, solid -->
  <g class="sticker solid navy" transform="translate(600 605)">
    <g clip-path="url(#sticker-shape)">
      <circle class="sticker-bg" r="176"/>
      <path class="contact-band" d="M-200 118 Q0 64 200 118 L200 200 L-200 200 Z"/>
    </g>
    <circle class="sticker-edge" r="176"/>
    <rect class="brand-square" x="-18" y="-156" width="36" height="36"/>
    <text class="brand-name" y="-80">VELUNORA</text>
    <text class="service-word service-word--single" y="44" textLength="335" lengthAdjust="spacingAndGlyphs">Gardening</text>
    <text class="contact" y="115">+39 320 5550147</text>
    <text class="contact" y="132">officevelunora.srl</text>
    <text class="contact" y="149">www.velunora.srl</text>
  </g>

  <!-- Pest Control, solid -->
  <g class="sticker solid green" transform="translate(998 605)">
    <g clip-path="url(#sticker-shape)">
      <circle class="sticker-bg" r="176"/>
      <path class="contact-band" d="M-200 118 Q0 64 200 118 L200 200 L-200 200 Z"/>
    </g>
    <circle class="sticker-edge" r="176"/>
    <rect class="brand-square" x="-18" y="-156" width="36" height="36"/>
    <text class="brand-name" y="-80">VELUNORA</text>
    <text class="service-word service-word--stacked" y="-8" textLength="120" lengthAdjust="spacingAndGlyphs">Pest</text>
    <text class="service-word service-word--stacked" y="52" textLength="255" lengthAdjust="spacingAndGlyphs" x="12">Control</text>
    <text class="contact" y="115">+39 320 5550147</text>
    <text class="contact" y="132">officevelunora.srl</text>
    <text class="contact" y="149">www.velunora.srl</text>
  </g>
</svg>
</body>
</html>
```